Hong Kong residential leasing and sales company needs a website design

Hong Kong has many competitive real estate agents. The majority of us have the same listings so, besides the team and experience, a website is what makes us stand out. A first impression. We need our website to be user friendly, informative and to have a wow factor. Most sites are generic so whilst we are close to accepting that maybe that's the only formula which works....we would like to see if we're missing something! Our clients are a mix of International users of all ages but probably ultimately 35+.. We have a logo (attached) which we would like to keep - designed by artmarketly. Flexible with colours except red.
examples of our competitors are:
http://www.brindlewoodestates.example
http://www.nuvo.example/home
http://www.premierdwellingsvx.example
http://www.orchid-lettings.example
http://www.tidemark-harrowgates.example
We were thinking of having the following in a menu bar with drop downs for most...some more than others. Home / For Sale / For Rent / Property 101 / About us / Contact Us ..
Look forward to seeing your ideas. Thanks in advance.

```html
<!DOCTYPE html>
<html lang="en">
<head>
<meta charset="utf-8">
<title>Harbourline Homes – Home</title>
<link rel="stylesheet" href="https://fonts.googleapis.com/css2?family=Cinzel:wght@400;500&family=Arimo:wght@400;700&family=Open+Sans:wght@400;600&display=swap">
<style>
:root{
  --purple:#7046a0;
  --purple-dark:#5e3689;
  --ink:#1f1f1f;
  --text:#555;
  --muted:#8a8a8a;
  --panel:#efefef;
  --line:#dcdcdc;
  --ribbon:#2b2b2b;
  --white:#fff;
}
*{box-sizing:border-box;margin:0;padding:0}
html,body{width:822px;height:1200px;overflow:hidden;background:var(--white)}
body{position:relative;font-family:"Arimo",Arial,sans-serif;color:var(--text)}
.top-rule{position:absolute;left:0;top:0;width:822px;height:3px;background:var(--ink)}
.site-header{position:absolute;left:0;top:3px;width:822px;height:121px}
.main-nav a{position:absolute;top:69px;font-family:"Cinzel",Georgia,serif;font-size:15px;color:var(--ink);text-decoration:none;letter-spacing:.2px}
.brand{position:absolute;left:336px;top:34px;width:150px;text-align:center;font-family:"Cinzel",Georgia,serif;font-weight:500;color:var(--purple);font-size:17px;letter-spacing:2px;line-height:20px}
.brand-mark{display:block;width:34px;height:34px;margin:0 auto 6px;background:var(--purple)}
.hero{position:absolute;left:0;top:124px;width:822px;height:357px;background:linear-gradient(180deg,#0b0f14 0%,#1e2733 35%,#3a4450 60%,#2a2418 85%,#4a3a12 100%)}
.search-panel{position:absolute;left:25px;top:123px;width:772px;height:100px;background:rgba(230,230,230,.88)}
.keyword{position:absolute;left:37px;top:18px;width:578px;height:30px;background:var(--white);font-family:"Cinzel",Georgia,serif;font-size:15px;color:#333;padding:6px 15px}
.select{position:absolute;top:59px;width:134px;height:25px;background:var(--white);font-family:"Open Sans",Arial,sans-serif;font-size:12px;color:#666;padding:4px 13px}
.select svg{position:absolute;right:12px;top:10px}
.search-btn{position:absolute;left:624px;top:18px;width:115px;height:67px;background:var(--purple);color:var(--white);font-family:"Open Sans",Arial,sans-serif;font-weight:600;font-size:11px;text-align:center;padding-top:8px;letter-spacing:.4px}
.search-btn svg{display:block;margin:0 auto 4px}
.featured-title{position:absolute;left:26px;top:508px;width:774px;height:39px;background:var(--purple);color:var(--white);font-family:"Cinzel",Georgia,serif;font-size:27px;padding:4px 22px;line-height:32px}
.featured{position:absolute;left:26px;top:547px;width:774px;height:512px;background:var(--panel)}
.card{position:absolute;width:164px;height:214px;background:var(--white);border:1px solid var(--line);overflow:hidden}
.photo{position:absolute;left:6px;top:6px;width:151px;height:113px}
.ribbon{position:absolute;left:0;top:0}
.card h3{position:absolute;left:6px;top:124px;font-size:11.5px;font-weight:700;color:var(--purple);white-space:nowrap}
.card ul{position:absolute;left:8px;top:143px;list-style:none;font-size:10px;line-height:12.2px;color:var(--text)}
.site-footer{position:absolute;left:0;top:1059px;width:822px;height:141px}
.footer-brand{position:absolute;left:32px;top:27px;width:88px;text-align:center;font-family:"Cinzel",Georgia,serif;font-weight:500;font-size:10px;color:var(--purple);letter-spacing:.5px;line-height:13px;white-space:nowrap}
.footer-brand .brand-mark{width:26px;height:26px;margin-bottom:6px}
.footer-blurb{position:absolute;left:127px;top:40px;width:175px;font-size:10px;line-height:12px;color:var(--muted)}
.copyright{position:absolute;left:35px;top:107px;font-size:9px;color:#333}
.footer-links{position:absolute;top:33px;list-style:none;font-size:10px;line-height:15px;color:#333}
.social{position:absolute;left:580px;top:31px;display:flex;gap:7px}
.social span{width:20px;height:20px;border-radius:50%;background:#111}
.address{position:absolute;left:581px;top:59px;font-size:9px;line-height:11.5px;color:#222;font-style:normal}
</style>
</head>
<body>
<div class="top-rule"></div>
<header class="site-header">
  <nav class="main-nav">
    <a style="left:29px">HOME</a>
    <a style="left:108px">PROPERTY 101</a>
    <a style="left:242px">FOR SALE</a>
    <a style="left:513px">FOR RENT</a>
    <a style="left:617px">ABOUT US</a>
    <a style="left:722px">CONTACT</a>
  </nav>
  <div class="brand"><span class="brand-mark"></span>HARBOURLINE<br>HOMES</div>
</header>

<section class="hero" role="img" aria-label="Night view of Hong Kong residential towers with lit windows above a glowing highway">
  <form class="search-panel">
    <div class="keyword">Keyword Search</div>
    <div class="select" style="left:37px">Property Type<svg width="8" height="6"><path d="M0 0H8L4 6Z" fill="#444"/></svg></div>
    <div class="select" style="left:184px">Sale/Rent<svg width="8" height="6"><path d="M0 0H8L4 6Z" fill="#444"/></svg></div>
    <div class="select" style="left:332px">Location<svg width="8" height="6"><path d="M0 0H8L4 6Z" fill="#444"/></svg></div>
    <div class="select" style="left:479px">Price Range<svg width="8" height="6"><path d="M0 0H8L4 6Z" fill="#444"/></svg></div>
    <div class="search-btn"><svg width="36" height="36" viewBox="0 0 36 36"><circle cx="15" cy="15" r="11" fill="none" stroke="#fff" stroke-width="3"/><path d="M23 23L33 33" stroke="#fff" stroke-width="4" stroke-linecap="round"/></svg>SEARCH</div>
  </form>
</section>

<h2 class="featured-title">FEATURED PROPERTIES</h2>
<section class="featured">
  <article class="card" style="left:26px;top:28px">
    <div class="photo" role="img" aria-label="Bright living room with harbour view windows" style="background:linear-gradient(160deg,#e8e4dc,#a89c8c 60%,#6e6358)"></div>
    <svg class="ribbon" width="70" height="70"><path d="M0 70V40L40 0H70Z" fill="var(--ribbon)"/><text x="17" y="48" transform="rotate(-45 17 48)" fill="#fff" font-size="10" font-family="Arimo, sans-serif">For Sale</text></svg>
    <h3>The Meridian - Block 02</h3>
    <ul><li>Gross Area: 3,850 sq.ft.</li><li>Saleable Area: 2,969 sq.ft.</li><li>Bedrooms: 4 (2 Ensuites)</li><li>Bathrooms: 3.5</li><li>Price: HK$ 260,000,000</li></ul>
  </article>
  <article class="card" style="left:211px;top:28px">
    <div class="photo" role="img" aria-label="Living room with red sofa and grand piano" style="background:linear-gradient(160deg,#d8d0c4,#9a7a6a 55%,#6a2a2a)"></div>
    <svg class="ribbon" width="70" height="70"><path d="M0 70V40L40 0H70Z" fill="var(--ribbon)"/><text x="17" y="48" transform="rotate(-45 17 48)" fill="#fff" font-size="10" font-family="Arimo, sans-serif">For Rent</text></svg>
    <h3>Casa Serena - Apartment B</h3>
    <ul><li>Gross Area: 2,700 sq.ft.</li><li>Saleable Area: 2,512 sq.ft.</li><li>Bedrooms: 3 (1 Ensuite)</li><li>Bathrooms: 2</li><li>Price: HK$ 75,000,000</li></ul>
  </article>
  <article class="card" style="left:396px;top:28px">
    <div class="photo" role="img" aria-label="City skyline above a green racecourse" style="background:linear-gradient(180deg,#a8c4e0,#d0d8e0 40%,#7a8a80 65%,#3e7a3a)"></div>
    <svg class="ribbon" width="70" height="70"><path d="M0 70V40L40 0H70Z" fill="var(--ribbon)"/><text x="17" y="48" transform="rotate(-45 17 48)" fill="#fff" font-size="10" font-family="Arimo, sans-serif">For Sale</text></svg>
    <h3>Paddock Heights</h3>
    <ul><li>Gross Area: 3,850 sq.ft.</li><li>Saleable Area: 2,969 sq.ft.</li><li>Bedrooms: 4 (2 Ensuites)</li><li>Bathrooms: 3.5</li><li>Price: HK$ 260,000,000</li></ul>
  </article>
  <article class="card" style="left:581px;top:28px">
    <div class="photo" role="img" aria-label="Living room with cream sofas and dark rug" style="background:linear-gradient(170deg,#e6e2dc,#b0a698 55%,#4a3c36)"></div>
    <svg class="ribbon" width="70" height="70"><path d="M0 70V40L40 0H70Z" fill="var(--ribbon)"/><text x="17" y="48" transform="rotate(-45 17 48)" fill="#fff" font-size="10" font-family="Arimo, sans-serif">For Sale</text></svg>
    <h3>Laurel Mansion</h3>
    <ul><li>Gross Area: 4,200 sq.ft.</li><li>Saleable Area: 3,273 sq.ft.</li><li>Bedrooms: 5 (3 Ensuites)</li><li>Bathrooms: 4</li><li>Price: HK$ 77,000,000</li></ul>
  </article>
  <article class="card" style="left:26px;top:271px">
    <div class="photo" role="img" aria-label="High-rise towers against a blue sky" style="background:linear-gradient(180deg,#3a6fb0,#a0bcd8 45%,#8a8a88 75%,#4a5a48)"></div>
    <svg class="ribbon" width="70" height="70"><path d="M0 70V40L40 0H70Z" fill="var(--ribbon)"/><text x="17" y="48" transform="rotate(-45 17 48)" fill="#fff" font-size="10" font-family="Arimo, sans-serif">For Rent</text></svg>
    <h3>Hillside Terrace 3</h3>
    <ul><li>Gross Area: 3,850 sq.ft.</li><li>Saleable Area: 2,969 sq.ft.</li><li>Bedrooms: 4 (2 Ensuites)</li><li>Bathrooms: 3.5</li><li>Price: HK$ 260,000,000</li></ul>
  </article>
  <article class="card" style="left:211px;top:271px">
    <div class="photo" role="img" aria-label="Warm living room with grey sofas" style="background:linear-gradient(170deg,#e4ddd2,#b4a490 55%,#6a5444)"></div>
    <svg class="ribbon" width="70" height="70"><path d="M0 70V40L40 0H70Z" fill="var(--ribbon)"/><text x="17" y="48" transform="rotate(-45 17 48)" fill="#fff" font-size="10" font-family="Arimo, sans-serif">For Sale</text></svg>
    <h3>Willow Court</h3>
    <ul><li>Gross Area: 2,700 sq.ft.</li><li>Saleable Area: 2,512 sq.ft.</li><li>Bedrooms: 3 (1 Ensuite)</li><li>Bathrooms: 2</li><li>Price: HK$ 75,000,000</li></ul>
  </article>
  <article class="card" style="left:396px;top:271px">
    <div class="photo" role="img" aria-label="White fitted kitchen with window" style="background:linear-gradient(170deg,#f2f0ec,#c8c4bc 55%,#8a8680)"></div>
    <svg class="ribbon" width="70" height="70"><path d="M0 70V40L40 0H70Z" fill="var(--ribbon)"/><text x="17" y="48" transform="rotate(-45 17 48)" fill="#fff" font-size="10" font-family="Arimo, sans-serif">For Sale</text></svg>
    <h3>Kestrel Towers - Block C</h3>
    <ul><li>Gross Area: 3,850 sq.ft.</li><li>Saleable Area: 2,969 sq.ft.</li><li>Bedrooms: 4 (2 Ensuites)</li><li>Bathrooms: 3.5</li><li>Price: HK$ 260,000,000</li></ul>
  </article>
  <article class="card" style="left:581px;top:271px">
    <div class="photo" role="img" aria-label="Living room with cream sofas and dark rug" style="background:linear-gradient(170deg,#e6e2dc,#b0a698 55%,#4a3c36)"></div>
    <svg class="ribbon" width="70" height="70"><path d="M0 70V40L40 0H70Z" fill="var(--ribbon)"/><text x="17" y="48" transform="rotate(-45 17 48)" fill="#fff" font-size="10" font-family="Arimo, sans-serif">For Rent</text></svg>
    <h3>Laurel Mansion</h3>
    <ul><li>Gross Area: 4,200 sq.ft.</li><li>Saleable Area: 3,273 sq.ft.</li><li>Bedrooms: 5 (3 Ensuites)</li><li>Bathrooms: 4</li><li>Price: HK$ 77,000,000</li></ul>
  </article>
</section>

<footer class="site-footer">
  <div class="footer-brand"><span class="brand-mark"></span>HARBOURLINE<br>HOMES</div>
  <p class="footer-blurb">Ut wisi enim ad minim veniam, quis nostrud exerci tation ullamcorper suscipit lobortis nisl ut aliquip ex ea commodo consequat.</p>
  <p class="copyright">Copyright ©2014 Harbourline Homes. All rights reserved.</p>
  <ul class="footer-links" style="left:351px"><li>Home</li><li>About Us</li><li>For Sale</li><li>For Rent</li><li>Property 101</li></ul>
  <ul class="footer-links" style="left:430px"><li>Contact</li><li>Privacy Policy</li><li>Terms</li><li>Disclaimer</li></ul>
  <div class="social" aria-label="Social links"><span></span><span></span><span></span><span></span><span></span></div>
  <address class="address">1601-1602 Meridian Commerce Centre, 8<br>Amberley Road, Central, Hong Kong<br>Tel: +852 2000 4810 / Fax: +852 2000 4811<br>info@harbourlinehomes.example</address>
</footer>
</body>
</html>
```